Vexel Business Cards

We need a new look business cvard to refelect our new look website www.vexel-example.com.au
We’re Vexel, a team of town planning and traffic and transport engineering specialists located in Melbourne.

Vexel is a company that is structured, articulate, dynamic, progressive, accurate and adaptable.
Our key messages are:
1. We make your life easier by doing what we do best
2. We tell you what you need to know not what you want to hear
3. Polished and professional but not afraid to show some personality

we would like a bold new look that is polished and professional but not afraid to show a bit of personality

Target Market(s)

Vexel’s diverse client base consists of architecture practices, builders, developers, local government and the legal fraternity.

Industry/Entity Type

Town

Requirements
Must have
• must use our logo and have the following information

Joel Harcastle
Director

Vexel Consultants Pty Ltd
Fernhollow first floor
Tamber Street
Calderbrook VIC 3999 Australia
+61 03 9555 0187
mail@vexel-example.com.au
www.vexel-example.com.au
Nice to have
• We would like to see the logo used or the colours of the logo used.

```html
<!DOCTYPE html>
<html lang="en">
<head>
<meta charset="utf-8">
<title>Vexel Business Cards</title>
<link rel="stylesheet" href="https://fonts.googleapis.com/css2?family=Open+Sans:wght@400&family=Arimo:ital,wght@0,400;0,700;1,400&family=Advent+Pro:wght@300&display=swap">
<style>
  :root {
    --stage: #f1f1f1;
    --card-grey: #d1d2d4;
    --card-white: #ffffff;
    --ink: #4f5a6b;
    --dot: #9a9ea5;
    --brand-blue: #1d93d8;
    --brand-green: #4cb848;
    --caption: #5d6470;
  }
  * { box-sizing: border-box; margin: 0; padding: 0; }
  html, body { width: 1200px; height: 1000px; overflow: hidden; }
  body {
    background: var(--stage);
    font-family: "Arimo", Arial, sans-serif;
    color: var(--ink);
    position: relative;
  }
  .card {
    position: absolute;
    width: 665px;
    height: 332px;
    border-radius: 22px;
    overflow: hidden;
    box-shadow: 0 2px 6px rgba(0,0,0,0.18);
  }
  .dotted {
    background-image: radial-gradient(circle, var(--dot) 1px, transparent 1.4px);
    background-size: 36px 36px;
    background-position: 14px 14px;
  }
  /* Front: brand side */
  .card-front { left: 160px; top: 90px; background-color: var(--card-grey); }
  .card-front .pattern-panel {
    position: absolute;
    top: 0; right: 0;
    width: 195px; height: 100%;
    background: linear-gradient(135deg, var(--brand-green) 0%, var(--brand-blue) 50%, var(--brand-green) 100%);
    clip-path: polygon(30px 0, 100% 0, 100% 100%, 30px 100%, 30px 62%, 0 52%, 30px 42%);
  }
  .card-front .wordmark {
    position: absolute;
    left: 120px; top: 88px;
    font-family: "Open Sans", Arial, sans-serif;
    font-weight: 400;
    font-size: 118px;
    letter-spacing: -2px;
    color: var(--ink);
    line-height: 1;
  }
  .card-front .website {
    position: absolute;
    left: 175px; top: 246px;
    font-weight: 700;
    font-size: 19px;
    color: var(--ink);
  }
  /* Back: contact side */
  .card-back { left: 335px; top: 467px; background-color: var(--card-grey); }
  .card-back .info-panel {
    position: absolute;
    top: 0; right: 0;
    width: 448px; height: 100%;
    background-color: var(--card-white);
    clip-path: polygon(30px 0, 100% 0, 100% 100%, 30px 100%, 30px 56%, 0 49%, 30px 42%);
  }
  .card-back .wordmark {
    position: absolute;
    left: 36px; top: 128px;
    font-family: "Open Sans", Arial, sans-serif;
    font-weight: 400;
    font-size: 60px;
    letter-spacing: -1px;
    line-height: 1;
    color: var(--ink);
  }
  .contact {
    position: absolute;
    left: 318px; top: 76px;
    font-size: 18.5px;
    line-height: 22px;
    color: var(--ink);
  }
  .contact .name { font-weight: 700; font-size: 19px; letter-spacing: 0.8px; }
  .contact .role { font-style: italic; font-size: 17px; margin-left: 10px; }
  .contact .phone { margin-top: 3px; margin-bottom: 25px; font-size: 17px; }
  .contact .email { margin-top: 16px; display: flex; align-items: center; gap: 7px; }
  .contact .email svg { width: 19px; height: 17px; }
  .caption {
    position: absolute;
    left: 48px; top: 840px;
    font-family: "Advent Pro", "Arial Narrow", sans-serif;
    font-weight: 300;
    font-size: 35px;
    line-height: 41px;
    color: var(--caption);
  }
</style>
</head>
<body>
  <section class="card card-front dotted">
    <div class="pattern-panel" role="img" aria-label="Blue, green and white checkered brand pattern"></div>
    <div class="wordmark">Vexel</div>
    <div class="website">www.vexel-example.com.au</div>
  </section>

  <section class="card card-back dotted">
    <div class="info-panel dotted"></div>
    <div class="wordmark">Vexel</div>
    <div class="contact">
      <div><span class="name">Joel Harcastle</span><span class="role">Director</span></div>
      <div class="phone">+61 03 9555 0187</div>
      <div>Vexel Consultants Pty Ltd</div>
      <div>Fernhollow first floor</div>
      <div>Tamber Street</div>
      <div>Calderbrook VIC 3999 Australia</div>
      <div class="email">
        <svg viewBox="0 0 18 16" aria-hidden="true">
          <rect x="0" y="0" width="18" height="16" rx="2" fill="#4f5a6b"/>
          <polyline points="2,4 9,9 16,4" fill="none" stroke="#ffffff" stroke-width="1.4"/>
        </svg>
        <span>mail@vexel-example.com.au</span>
      </div>
    </div>
  </section>

  <div class="caption">
    <div>Namecard Round Corner Cut</div>
    <div>Size: 9cm(h)x4.5cm(w)</div>
    <div>Special Print: Logo name in UV varnish effect</div>
  </div>
</body>
</html>
```